High-End Bifold Brochure for Aesthetics Medspa Business

I need a print-ready, bifold brochure designed for a high-end, luxurious Aesthetics/Medspa practice.

The brochure will showcase the latest IV Therapy content (6 options included in MENU.docx), and exclusive Vitamin B12+ wellness shot content (included in VB PDF). It should also include the business logo and basic office contact options.

The design should be clean, modern, and appealing with a light design. It should flow nicely and compliment the website theme/design. Preferably, having the 6 IV treatments inside bifold, with B12 shot on back/outside page. For easy viewing.

I have attached a few licensed images, if you think they will incorporate into the design nicely. Otherwise, please ignore them. If needed, I can send more.

https://velorabloomclinic.com/
Brand purple: #491c64
Fonts used on site:
Josefin Sans
Montserrat

Size should be 6.5 x 9 using specs on Quellpress's template page (Half Fold design)
https://www.quellpress.com/resources/templates

Font styles to use
Other font styles liked:
• Montserrat, Josefin Sans, or similar

Requirements
Must have
• Content included in MENU + B12 shot content on PDF.
Similar feel to the website, High-end, modern, luxurious

```html
<!DOCTYPE html>
<html lang="en">
<head>
<meta charset="utf-8">
<title>Velora Bloom Aesthetics – Bifold Brochure</title>
<link href="https://fonts.googleapis.com/css2?family=Montserrat:wght@300;400;500;600;700;800&family=Josefin+Sans:wght@300;400;600&display=swap" rel="stylesheet">
<style>
:root{
  --purple:#491c64;
  --purple-mid:#5e2d80;
  --purple-soft:#7a4c98;
  --ink:#3a3340;
  --muted:#6d6672;
  --paper:#f7f6f7;
  --stage:#e6e6e6;
  --white:#ffffff;
}
*{margin:0;padding:0;box-sizing:border-box}
html,body{width:1200px;height:2810px;overflow:hidden}
body{background:var(--stage);font-family:"Montserrat",sans-serif;color:var(--ink);position:relative}
.page{position:absolute;width:550px;height:762px;background:var(--paper);overflow:hidden}
.spread{position:absolute;left:50px;width:1100px;height:762px;box-shadow:0 18px 40px rgba(0,0,0,.18)}
.spread .page{top:0}
.spread .page.left{left:0}
.spread .page.right{left:550px}
.solo{left:325px;top:50px;box-shadow:0 18px 40px rgba(0,0,0,.18)}
.fill{position:absolute}

/* cover */
.cover .interior{left:0;top:0;width:550px;height:762px;background:linear-gradient(160deg,#fafafa 0%,#ecebed 45%,#d9d7da 100%)}
.cover .dark-panel{left:340px;top:0;width:210px;height:560px;background:linear-gradient(180deg,#3b3b3d,#565658)}
.cover .portrait{left:190px;top:55px;width:340px;height:600px;border-radius:170px 170px 0 0;background:radial-gradient(ellipse at 45% 30%,#c79a82 0%,#7a4f3b 40%,#3a2620 75%,#1e1a1b 100%)}
.cover .tagline{position:absolute;left:78px;top:470px;transform:rotate(-90deg);transform-origin:0 0;font-family:"Josefin Sans",sans-serif;color:var(--purple);font-size:34px;line-height:40px;letter-spacing:1px;font-weight:400;white-space:nowrap}
.cover .band{position:absolute;left:0;top:0}
.cover .brand-line{position:absolute;left:80px;top:668px;transform:rotate(-14deg);transform-origin:0 0;color:var(--white);display:flex;align-items:center;gap:12px}
.brand-mark{width:36px;height:36px;border:2px solid var(--white);border-radius:50%}
.brand-name{font-family:"Montserrat",sans-serif;font-weight:600;font-size:16px;letter-spacing:1px;text-transform:uppercase}
.cover .web{position:absolute;left:70px;top:730px;transform:rotate(-14deg);transform-origin:0 0;color:var(--white);font-size:15px;letter-spacing:4px;font-weight:400;white-space:nowrap}

/* back page */
.back .interior{left:0;top:0;width:550px;height:480px;background:linear-gradient(180deg,#fbfbfb,#eeedef)}
.back .doctor{left:215px;top:30px;width:120px;height:120px;border-radius:50%;border:4px solid var(--purple-soft);background:radial-gradient(circle at 50% 40%,#c8a08e,#4a3a44 60%,#2b2630)}
.back .doc-name{position:absolute;top:160px;width:100%;text-align:center;color:var(--purple);font-weight:700;font-size:15px}
.back .doc-cred{position:absolute;top:180px;width:100%;text-align:center;font-size:11px;letter-spacing:1px}
.back .doc-intro{position:absolute;top:205px;left:70px;width:410px;text-align:center;font-size:8.5px;font-weight:700;line-height:12px;text-transform:uppercase}
.back .bio{position:absolute;top:260px;left:70px;width:410px;font-size:8.5px;line-height:12.5px;color:var(--muted)}
.back .bio p{margin-bottom:7px}
.back .building{left:0;top:440px;width:550px;height:200px;background:linear-gradient(180deg,#c99378 0%,#9e6b57 50%,#5a3c36 100%)}
.back .contact-band{position:absolute;left:0;top:625px;width:550px;height:137px;background:var(--purple);clip-path:polygon(0 12%,100% 0,100% 100%,0 100%)}
.back .call{position:absolute;top:665px;width:100%;text-align:center;color:var(--white);font-size:17px;letter-spacing:1px}
.back .call b{font-weight:700}
.back .rule{position:absolute;top:695px;left:135px;width:280px;height:1px;background:rgba(255,255,255,.7)}
.back .address{position:absolute;top:705px;width:100%;text-align:center;color:var(--white);font-size:11px;line-height:15px}

/* inside left */
.b12 .header{left:0;top:0;width:550px;height:200px;background:linear-gradient(135deg,var(--purple),var(--purple-mid))}
.b12 .kicker{position:absolute;top:30px;left:300px;color:var(--white);font-size:13px;font-weight:700}
.b12 .title{position:absolute;top:52px;left:300px;color:#e7dcef;font-family:"Josefin Sans",sans-serif;font-size:27px;line-height:30px;font-weight:300}
.b12 .vitamin-card{position:absolute;left:28px;top:70px;width:265px;height:470px;background:var(--white);padding:22px 18px;box-shadow:0 4px 14px rgba(0,0,0,.08)}
.vitamin{margin-bottom:12px;padding-left:14px;position:relative}
.vitamin::before{content:"";position:absolute;left:0;top:3px;width:6px;height:6px;background:var(--purple);border-radius:50%}
.vitamin h4{font-size:9.5px;font-weight:700;letter-spacing:.5px;color:var(--ink)}
.vitamin p{font-size:7.5px;line-height:10.5px;color:var(--muted)}
.b12 .products{left:330px;top:230px;width:190px;height:150px;background:linear-gradient(160deg,#f3f1ef,#d7cfc4 60%,#b9ab9a)}
.b12 .benefits-title{position:absolute;left:330px;top:395px;color:var(--purple);font-family:"Josefin Sans",sans-serif;font-size:24px;line-height:26px}
.b12 .benefits-title b{font-family:"Montserrat",sans-serif;font-weight:800;display:block;font-size:22px}
.b12 .benefits{position:absolute;left:330px;top:460px;width:195px;list-style:none}
.b12 .benefits li{font-size:8px;line-height:11px;color:var(--muted);margin-bottom:7px;padding-left:12px;position:relative}
.b12 .benefits li::before{content:"";position:absolute;left:0;top:2px;width:6px;height:6px;background:var(--purple);border-radius:50%}
.b12 .team{left:28px;top:560px;width:265px;height:180px;background:linear-gradient(135deg,#b9b7c0,#6e6b78 55%,#2e2a33)}

/* inside right */
.iv .face{left:0;top:0;width:550px;height:330px;background:linear-gradient(90deg,#5b2d78 0%,#8b5a94 35%,#d9b6ad 70%,#f1ddd4 100%)}
.iv .title{position:absolute;left:40px;top:350px;color:var(--purple);font-size:22px;font-weight:800;line-height:24px}
.iv .subtitle{position:absolute;left:40px;top:400px;color:var(--purple-soft);font-family:"Josefin Sans",sans-serif;font-size:20px;letter-spacing:1px;font-weight:300}
.iv .col{position:absolute;width:235px}
.iv .col.a{left:30px;top:450px}
.iv .col.b{left:285px;top:355px}
.treatment{display:flex;gap:10px;margin-bottom:16px}
.price{flex:0 0 46px;height:46px;border-radius:50%;background:var(--purple);color:var(--white);font-size:12px;font-weight:500;display:flex;align-items:center;justify-content:center;border:2px solid #d9cce3;box-shadow:0 0 0 2px var(--purple)}
.treatment h3{font-size:11px;font-weight:800;color:var(--purple);line-height:13px;text-transform:uppercase;margin-top:4px}
.treatment p{font-size:7.5px;line-height:10.5px;color:var(--muted);margin-top:3px}
</style>
</head>
<body>

<!-- Front cover -->
<section class="page cover solo">
  <div class="fill interior" role="img" aria-label="Soft white medspa interior background"></div>
  <div class="fill dark-panel"></div>
  <div class="fill portrait" role="img" aria-label="Portrait photo of a woman with long wavy brown hair in a black dress"></div>
  <div class="tagline">TUCSON'S<br>PREMIER MEDSPA</div>
  <svg class="band" width="550" height="762" viewBox="0 0 550 762">
    <polygon points="0,640 550,500 550,545 0,685" fill="#7a4c98" opacity=".75"/>
    <polygon points="0,660 550,520 550,640 0,780" fill="#491c64"/>
  </svg>
  <div class="brand-line"><span class="brand-mark"></span><span class="brand-name">Velora Bloom Aesthetics</span></div>
  <div class="web">www.velorabloomclinic.com</div>
</section>

<!-- Outside spread -->
<section class="spread" style="top:930px">
  <article class="page left back">
    <div class="fill interior" role="img" aria-label="Bright white clinic treatment room"></div>
    <div class="fill doctor" role="img" aria-label="Portrait photo of the medical director"></div>
    <div class="doc-name">Dr. Adrian Venholt</div>
    <div class="doc-cred">M.D.,F.A.C.S.</div>
    <div class="doc-intro">Tucson's top rated facial rejuvenation &amp; aesthetics physician specializing in the gold standard of facial rejuvenation using the most advanced techniques available.</div>
    <div class="bio">
      <p>As founder and medical director of Velora Bloom Aesthetics, Dr. Venholt brings decades of surgical experience and a passion for natural, refreshed results.</p>
      <p>His expertise spans facial plastic surgery, injectables and advanced skin care, offering each patient a personal plan built around their goals.</p>
      <p>Dr. Venholt has been recognized by his peers for excellence in care and trains physicians nationwide in modern aesthetic techniques.</p>
    </div>
    <div class="fill building" role="img" aria-label="Photo of the clinic building entrance at dusk"></div>
    <div class="contact-band"></div>
    <div class="call">CALL US <b>(520) 555-0147</b></div>
    <div class="rule"></div>
    <div class="address">4120 E Marigold Ridge Unit 12<br>Tucson, Arizona 85718</div>
  </article>

  <article class="page right cover">
    <div class="fill interior" role="img" aria-label="Soft white medspa interior background"></div>
    <div class="fill dark-panel"></div>
    <div class="fill portrait" role="img" aria-label="Portrait photo of a woman with long wavy brown hair in a black dress"></div>
    <div class="tagline">TUCSON'S<br>PREMIER MEDSPA</div>
    <svg class="band" width="550" height="762" viewBox="0 0 550 762">
      <polygon points="0,640 550,500 550,545 0,685" fill="#7a4c98" opacity=".75"/>
      <polygon points="0,660 550,520 550,640 0,780" fill="#491c64"/>
    </svg>
    <div class="brand-line"><span class="brand-mark"></span><span class="brand-name">Velora Bloom Aesthetics</span></div>
    <div class="web">www.velorabloomclinic.com</div>
  </article>
</section>

<!-- Inside spread -->
<section class="spread" style="top:1820px">
  <article class="page left b12">
    <div class="fill header"></div>
    <div class="kicker">Dr. Venholt's Vitamin B12 Cocktail's</div>
    <div class="title">Essential Vitamins<br>And Nutrients</div>
    <div class="vitamin-card">
      <div class="vitamin"><h4>THIAMINE</h4><p>Helps the body turn food into energy and supports nerve function.</p></div>
      <div class="vitamin"><h4>RIBOFLAVIN</h4><p>Supports energy production and healthy skin, eyes and cells.</p></div>
      <div class="vitamin"><h4>NIACINAMIDE</h4><p>Aids circulation and helps keep skin calm, clear and hydrated.</p></div>
      <div class="vitamin"><h4>PYRIDOXINE</h4><p>Supports mood, brain health and a strong immune response.</p></div>
      <div class="vitamin"><h4>HYDROXOCOBALAMIN</h4><p>Long lasting B12 that boosts energy and red blood cell health.</p></div>
      <div class="vitamin"><h4>METHIONINE</h4><p>Amino acid that helps the liver process fats and toxins.</p></div>
      <div class="vitamin"><h4>INOSITOL</h4><p>Supports healthy metabolism, hair growth and balanced mood.</p></div>
      <div class="vitamin"><h4>L-CARNITINE</h4><p>Helps the body burn stored fat for lasting energy.</p></div>
      <div class="vitamin"><h4>CHROMIUM</h4><p>Helps balance blood sugar and curb unwanted cravings.</p></div>
    </div>
    <div class="fill products" role="img" aria-label="Photo of skin care bottles with an orchid and woven basket"></div>
    <div class="benefits-title">OVERALL<b>BENEFITS</b></div>
    <ul class="benefits">
      <li>Boosts natural energy and helps fight daily fatigue.</li>
      <li>Supports a healthy metabolism and weight goals.</li>
      <li>Helps improve mood, focus and mental clarity.</li>
      <li>Promotes healthy skin, hair and nails.</li>
      <li>Strengthens the immune system year round.</li>
      <li>Aids restful sleep and faster recovery.</li>
    </ul>
    <div class="fill team" role="img" aria-label="Group photo of the clinic team in black uniforms"></div>
  </article>

  <article class="page right iv">
    <div class="fill face" role="img" aria-label="Close-up beauty photo of a woman with glowing skin"></div>
    <div class="title">THE DRIP<br>LOUNGE</div>
    <div class="subtitle">IV THERAPY</div>
    <div class="col a">
      <div class="treatment"><div class="price">$100</div><div><h3>Refresh<br>&amp; Hydrate</h3><p>Rehydrate from the inside out with fluids and electrolytes that restore balance fast.</p></div></div>
      <div class="treatment"><div class="price">$150</div><div><h3>Migraine<br>Buster</h3><p>Calms headache pain and nausea so you can get back to your day.</p></div></div>
      <div class="treatment"><div class="price">$150</div><div><h3>Immunity<br>Booster</h3><p>A blend of vitamin C and zinc to help your body fight off illness.</p></div></div>
    </div>
    <div class="col b">
      <div class="treatment"><div class="price">$180</div><div><h3>Wellness<br>Infusion</h3><p>Our classic vitamin cocktail for energy, immunity and overall vitality.</p></div></div>
      <div class="treatment"><div class="price">$200</div><div><h3>Glo</h3><p>A beauty blend of glutathione and biotin for bright, radiant skin.</p></div></div>
      <div class="treatment"><div class="price">$200</div><div><h3>The Ultimate<br>Weight Loss Infusion</h3><p>Fat burning nutrients that support metabolism and steady energy.</p></div></div>
      <div class="treatment"><div class="price">$300</div><div><h3>NAD+ IV:<br>The Fountain of Youth (+)</h3><p>Anti-aging support that restores cell energy, focus and clarity.</p></div></div>
    </div>
  </article>
</section>

</body>
</html>
```